Promotion for Local Garage - Orwin Motorworks offering 10% off

We are after an A5 Colour Leaflet to promote our business Orwin Motorworks.

Orwin Motorworks is a local garage and we are about to launch a flyer campaign in the local area.

Services we provide:
Servicing, Repairs, Diagnostics, Clutches, Brakes, Exhaust for all makes and models of cars and vans.

10% discount for anyone who brings in this flyer with them.

Company contact details below:
Telephone 0151 3846172
Website www.orwinmotors-example.co.uk

Address
Unit 4 Hollin Workshops,
Brackwell Lane,
Fenwick Ind Estate,
Ellesmere Port,
CH64 9QP

Our Logo is attached

Target Market(s)

Local Residents and businesses

Industry/Entity Type

Auto Repair

Requirements
Must have
• Services we provide:
• Servicing, Repairs, Diagnostics, Clutches, Brakes, Exhaust for all makes and models of cars and vans.
• 10% discount for anyone who brings in this flyer with them.
• Company contact details below:
• Telephone 0151 3846172
• Website www.orwinmotors-example.co.uk
• Address
• Unit 4 Hollin Workshops,
• Brackwell Lane,
• Fenwick Ind Estate,
• Ellesmere Port,
• CH64 9QP

```html
<!DOCTYPE html>
<html lang="en">
<head>
<meta charset="utf-8">
<title>Orwin Motorworks – A5 Leaflet</title>
<link href="https://fonts.googleapis.com/css2?family=Open+Sans:wght@300;400;600;700;800&display=swap" rel="stylesheet">
<style>
  :root {
    --brand-red: #e31e24;
    --panel-grey: #58585a;
    --ink: #333333;
    --paper: #ffffff;
    --backdrop: #e6e7e9;
  }
  * { margin: 0; padding: 0; box-sizing: border-box; }
  html, body {
    width: 1200px; height: 1200px; overflow: hidden;
    background: var(--backdrop);
    font-family: "Open Sans", sans-serif;
  }
  .leaflet {
    position: absolute; left: 206px; top: 40px;
    width: 940px; height: 1335px;
    background: var(--paper);
    transform: scale(0.839); transform-origin: top left;
    box-shadow: 0 6px 24px rgba(0,0,0,.18);
    overflow: hidden;
  }
  .hero { position: absolute; left: 0; top: 0; width: 940px; height: 668px; display: block; }
  .hero-band { position: absolute; left: 0; top: 668px; width: 940px; height: 12px; background: var(--brand-red); }

  .booking {
    position: absolute; right: 95px; top: 132px;
    text-align: right; color: var(--paper);
  }
  .booking-prompt { font-size: 30px; font-weight: 400; line-height: 34.5px; letter-spacing: .3px; }
  .booking-phone { font-size: 55px; font-weight: 700; line-height: 64px; margin-top: 6px; letter-spacing: -.5px; }

  .services { position: absolute; left: 95px; top: 728px; width: 294px; height: 512px; background: var(--panel-grey); }
  .services-title {
    height: 64px; background: var(--brand-red); color: var(--paper);
    font-size: 34px; font-weight: 700; text-align: center; line-height: 64px;
  }
  .services-list {
    color: var(--paper); font-size: 30px; font-weight: 400;
    text-align: center; line-height: 43px; padding-top: 32px;
  }

  .brand { position: absolute; left: 437px; top: 778px; display: flex; align-items: center; gap: 14px; }
  .brand-mark { width: 22px; height: 22px; border-radius: 50%; background: var(--brand-red); }
  .brand-name { font-size: 40px; font-weight: 600; color: var(--panel-grey); letter-spacing: .3px; }

  .website { position: absolute; left: 437px; top: 866px; font-size: 26px; font-weight: 700; color: var(--brand-red); white-space: nowrap; }
  .address { position: absolute; left: 437px; top: 928px; font-size: 26px; font-weight: 400; line-height: 30px; color: var(--ink); font-style: normal; }

  .offer {
    position: absolute; left: 437px; top: 1126px; width: 503px; height: 114px;
    background: var(--brand-red); color: var(--paper);
    text-align: right; padding-right: 95px; padding-top: 10px;
  }
  .offer-lead { font-size: 30px; font-weight: 400; line-height: 38px; }
  .offer-amount { font-size: 56px; font-weight: 800; line-height: 58px; letter-spacing: -.5px; }
</style>
</head>
<body>
  <main class="leaflet">
    <svg class="hero" viewBox="0 0 940 668" xmlns="http://www.w3.org/2000/svg">
      <defs>
        <linearGradient id="workshop" x1="0" y1="0" x2="1" y2="1">
          <stop offset="0" stop-color="#c9d3de"/>
          <stop offset=".45" stop-color="#3d5e9c"/>
          <stop offset="1" stop-color="#2a78b8"/>
        </linearGradient>
        <linearGradient id="mechanic" x1="0" y1="0" x2="1" y2="0">
          <stop offset="0" stop-color="#1e2533"/>
          <stop offset=".5" stop-color="#6b6560"/>
          <stop offset="1" stop-color="#b9ada0"/>
        </linearGradient>
        <radialGradient id="engine" cx=".6" cy=".5" r=".7">
          <stop offset="0" stop-color="#8a8c90"/>
          <stop offset="1" stop-color="#1d1e20"/>
        </radialGradient>
      </defs>
      <rect x="0" y="0" width="940" height="333" fill="var(--panel-grey)"/>
      <polygon points="0,0 614,0 424,333 0,333" fill="var(--brand-red)"/>
      <polygon role="img" aria-label="Photo of a blue van and a car on lifts in the workshop" points="0,0 600,0 410,333 0,333" fill="url(#workshop)"/>
      <rect role="img" aria-label="Close-up photo of an engine bay and alternator" x="0" y="333" width="940" height="335" fill="url(#engine)"/>
      <polygon points="0,333 576,333 378,668 0,668" fill="var(--brand-red)"/>
      <polygon role="img" aria-label="Photo of a mechanic holding a diagnostic tool over an open bonnet" points="0,333 562,333 362,668 0,668" fill="url(#mechanic)"/>
    </svg>
    <div class="hero-band"></div>

    <section class="booking">
      <p class="booking-prompt">BOOK YOUR<br>APPOINTMENT NOW<br>OR CALL</p>
      <p class="booking-phone">0151 3846172</p>
    </section>

    <section class="services">
      <h2 class="services-title">OUR SERVICES</h2>
      <p class="services-list">Servicing,<br>Repairs,<br>Diagnostics,<br>Clutches,<br>Brakes,<br>Exhaust for all<br>makes and<br>models of cars<br>and vans</p>
    </section>

    <div class="brand">
      <span class="brand-name">Orwin Motorworks</span>
      <span class="brand-mark"></span>
    </div>
    <p class="website">www.orwinmotors-example.co.uk</p>
    <address class="address">Unit 4 Hollin Workshops,<br>Brackwell Lane,<br>Fenwick Ind Estate,<br>Ellesmere Port,<br>CH64 9QP</address>

    <section class="offer">
      <p class="offer-lead">brings this flyer and get</p>
      <p class="offer-amount">10% discount</p>
    </section>
  </main>
</body>
</html>
```